Marvantar - Seafood industry professional promoting page

Hi. I´m in the seafood business with a one man company sourcing and exporting frozen seafood. I need to make a one page homepage for Marvantar (from Iceland). The feeling of it should be; Trustworthy, experience and knowledge.
Using as background a picture (or part of it), or a moving video:

http://www1.brelvik.is/sjorinn/myndir/ufsinn.jpg
https://clipvera.com/583720415

Main text to be:

- We can help source, market and add value to your seafood business
- Years of experience in seafood trade and production
- Extensive knowledge of fishing, seasonality, production and accreditations

Contact:
dagur@marvantar.is
Tel: +3654170392
(with a photo)

p.s. please also make logo look better.

Target Market(s)

Seafood industry

Industry/Entity Type

Business

Logo Text

Marvantar

Coding

Coded - Design and coding required

Number of Pages Required

1 page

Colors
0792cd
33a6d7

```html
<!DOCTYPE html>
<html lang="en">
<head>
<meta charset="utf-8">
<title>Marvantar – Seafood sourcing and export</title>
<link rel="stylesheet" href="https://fonts.googleapis.com/css2?family=Roboto:wght@400;500;700&family=Roboto+Condensed:wght@300;400;700&display=swap">
<style>
  :root {
    --brand: #0792cd;
    --brand-deep: #0b79bd;
    --brand-light: #33a6d7;
    --ink: #222;
    --body: #3a3a3a;
    --white: #fff;
    --footer: #0a7cc2;
    --footer-text: #b7dcf1;
  }
  * { box-sizing: border-box; margin: 0; padding: 0; }
  html, body { width: 1200px; height: 2368px; overflow: hidden; }
  body { font-family: "Roboto", Arial, sans-serif; color: var(--body); background: var(--white); position: relative; }

  .site-header { position: absolute; top: 0; left: 0; width: 1200px; height: 106px; background: var(--white); z-index: 2; box-shadow: 0 2px 6px rgba(0,0,0,.12); }
  .brand { position: absolute; left: 101px; top: 12px; display: flex; align-items: center; gap: 12px; }
  .brand-mark { width: 82px; height: 82px; border-radius: 50%; background: var(--brand); }
  .brand-name { font-weight: 700; font-size: 40px; color: var(--brand); letter-spacing: -0.5px; }
  .main-nav { position: absolute; top: 45px; left: 0; width: 1200px; }
  .main-nav a { position: absolute; font-size: 13.5px; text-transform: uppercase; color: var(--ink); text-decoration: none; white-space: nowrap; transform: translateX(-50%); }
  .main-nav a.is-active { color: var(--brand); }

  .hero { position: absolute; top: 106px; left: 0; width: 1200px; height: 556px; overflow: hidden; }
  .hero-bg { position: absolute; inset: 0; background: radial-gradient(ellipse at 70% 60%, #8fcbe8 0%, #3c97cf 45%, #1b6aa8 100%); }
  .hero-title { position: absolute; top: 100px; width: 100%; text-align: center; color: var(--white); font-weight: 700; font-size: 32px; }
  .slider-arrow { position: absolute; top: 208px; width: 48px; height: 48px; border-radius: 50%; background: rgba(20,60,100,.45); }
  .slider-arrow svg { width: 48px; height: 48px; }
  .slider-arrow.prev { left: 20px; }
  .slider-arrow.next { left: 1116px; }
  .video-frame { position: absolute; left: 390px; top: 166px; width: 420px; height: 336px; border: 3px solid #e8f3fa; background: linear-gradient(180deg, #3fd3d6 0%, #1d8b8a 45%, #0f4d4c 100%); }
  .video-frame .play { position: absolute; left: 174px; top: 130px; width: 72px; height: 72px; }
  .video-frame .tools { position: absolute; right: 6px; top: 6px; display: flex; flex-direction: column; gap: 5px; }
  .video-frame .tools span { width: 22px; height: 21px; background: rgba(0,0,0,.75); border-radius: 2px; }
  .video-frame .controls { position: absolute; left: 0; bottom: 0; width: 100%; height: 30px; background: rgba(0,0,0,.55); }
  .video-frame .controls svg { width: 100%; height: 30px; }

  .welcome { position: absolute; top: 662px; left: 0; width: 1200px; height: 374px; text-align: center; }
  .welcome h1 { position: absolute; top: 52px; width: 100%; font-family: "Roboto Condensed", Arial, sans-serif; font-weight: 700; font-size: 44px; color: var(--brand); }
  .welcome p { position: absolute; left: 125px; width: 950px; font-size: 13.5px; line-height: 26.5px; color: var(--body); }
  .welcome .p1 { top: 125px; }
  .welcome .p2 { top: 228px; }

  .experience { position: absolute; top: 1036px; left: 0; width: 1200px; height: 374px; overflow: hidden; text-align: center; color: var(--white); }
  .experience-bg { position: absolute; inset: 0; background: linear-gradient(120deg, #3b8fae 0%, #2e86c4 40%, #3a93cc 70%, #2a7fbd 100%); }
  .experience h2 { position: absolute; top: 70px; width: 100%; font-family: "Roboto Condensed", Arial, sans-serif; font-weight: 300; font-size: 44px; }
  .experience p { position: absolute; top: 141px; left: 172px; width: 856px; font-size: 13.5px; line-height: 23px; }
  .outline-btn { display: inline-block; border: 2px solid currentColor; text-transform: uppercase; text-decoration: none; text-align: center; font-weight: 500; }
  .experience .outline-btn { position: absolute; left: 515px; top: 1248px; top: 248px; width: 170px; height: 50px; line-height: 46px; color: var(--white); font-size: 17px; border-color: rgba(255,255,255,.85); }

  .services { position: absolute; top: 1410px; left: 0; width: 1200px; height: 534px; text-align: center; }
  .services h2 { position: absolute; top: 60px; width: 100%; font-family: "Roboto Condensed", Arial, sans-serif; font-weight: 700; font-size: 44px; color: var(--ink); }
  .service { position: absolute; top: 162px; width: 330px; }
  .service:nth-of-type(1) { left: 64px; }
  .service:nth-of-type(2) { left: 435px; }
  .service:nth-of-type(3) { left: 805px; }
  .service-icon { width: 124px; height: 124px; margin: 0 auto; display: block; }
  .service h3 { margin-top: 20px; font-weight: 400; font-size: 16px; text-transform: uppercase; color: var(--ink); }
  .service p { width: 250px; margin: 8px auto 0; font-size: 13px; line-height: 19.5px; color: var(--body); }
  .service .outline-btn { margin-top: 19px; width: 130px; height: 36px; line-height: 32px; color: var(--brand); font-size: 15px; }

  .contact { position: absolute; top: 1944px; left: 0; width: 1200px; height: 350px; overflow: hidden; color: var(--white); }
  .contact-bg { position: absolute; inset: 0; background: linear-gradient(180deg, #2b86c2 0%, #3795cd 55%, #2a83c0 100%); }
  .contact h2 { position: absolute; top: 60px; width: 100%; text-align: center; font-family: "Roboto Condensed", Arial, sans-serif; font-weight: 700; font-size: 44px; }
  .contact-photo { position: absolute; left: 390px; top: 154px; width: 120px; height: 120px; border-radius: 50%; background: radial-gradient(circle at 50% 35%, #f7c27a 0%, #d9884a 45%, #6a4a3c 100%); }
  .contact-list { position: absolute; left: 557px; top: 184px; list-style: none; font-size: 20px; line-height: 36px; }
  .contact-list li { display: flex; align-items: center; gap: 6px; }
  .contact-list svg { width: 18px; height: 18px; }

  .site-footer { position: absolute; top: 2294px; left: 0; width: 1200px; height: 74px; background: var(--footer); color: var(--footer-text); text-align: center; font-size: 15px; line-height: 74px; }
</style>
</head>
<body>
  <header class="site-header">
    <div class="brand"><span class="brand-mark"></span><span class="brand-name">Marvantar</span></div>
    <nav class="main-nav">
      <a class="is-active" href="#" style="left:550px">Home</a>
      <a href="#" style="left:641px">About us</a>
      <a href="#" style="left:758px">Our services</a>
      <a href="#" style="left:876px">Features</a>
      <a href="#" style="left:965px">Blog</a>
      <a href="#" style="left:1061px">Contact us</a>
    </nav>
  </header>

  <section class="hero">
    <div class="hero-bg" role="img" aria-label="Blurred underwater photo of fish swimming in blue water"></div>
    <h2 class="hero-title">We can help source, market and add value to your seafood business</h2>
    <span class="slider-arrow prev"><svg viewBox="0 0 48 48"><path d="M28 14 L18 24 L28 34" fill="none" stroke="#fff" stroke-width="1.6"/></svg></span>
    <span class="slider-arrow next"><svg viewBox="0 0 48 48"><path d="M20 14 L30 24 L20 34" fill="none" stroke="#fff" stroke-width="1.6"/></svg></span>
    <div class="video-frame" role="img" aria-label="Video of a school of cod swimming underwater">
      <div class="tools"><span></span><span></span><span></span><span></span></div>
      <svg class="play" viewBox="0 0 72 72"><circle cx="36" cy="36" r="33" fill="none" stroke="rgba(255,255,255,.6)" stroke-width="3"/><path d="M28 22 L52 36 L28 50 Z" fill="none" stroke="rgba(255,255,255,.6)" stroke-width="3"/></svg>
      <div class="controls"><svg viewBox="0 0 414 30"><path d="M16 9 L26 15 L16 21 Z" fill="#fff"/><rect x="42" y="14" width="300" height="2" fill="rgba(255,255,255,.5)"/><rect x="356" y="12" width="14" height="8" fill="#33a6d7"/><circle cx="384" cy="15" r="4" fill="#fff"/><rect x="396" y="11" width="8" height="8" fill="none" stroke="#fff" stroke-width="1.5"/></svg></div>
    </div>
  </section>

  <section class="welcome">
    <h1>Welcome to Marvantar</h1>
    <p class="p1">Sed ut perspiciatis unde omnis iste natus error sit voluptatem accusantium doloremque laudantium, totam rem aperiam, eaque ipsa quae ab illo inventore veritatis et quasi architecto beatae vitae dicta sunt explicabo. Nemo enim ipsam voluptatem quia voluptas sit aspernatur aut odit aut fugit, sed quia consequuntur magni dolores eos qui ratione voluptatem sequi nesciunt.</p>
    <p class="p2">Neque porro quisquam est, qui dolorem ipsum quia dolor sit amet, consectetur, adipisci velit, sed quia non numquam eius modi tempora incidunt ut labore et dolore magnam aliquam quaerat voluptatem. Ut enim ad minima veniam.</p>
  </section>

  <section class="experience">
    <div class="experience-bg" role="img" aria-label="Close-up photo of fresh fish on ice, tinted blue"></div>
    <h2>Years of experience in seafood trade and production</h2>
    <p>At vero eos et accusamus et iusto odio dignissimos ducimus qui blanditiis praesentium voluptatum deleniti atque corrupti quos dolores et quas molestias excepturi sint occaecati cupiditate non provident, similique sunt in culpa qui officia deserunt mollitia animi, id est laborum et dolorum fuga. Et harum quidem rerum facilis est et expedita distinctio.</p>
    <a class="outline-btn" href="#">Learn more</a>
  </section>

  <section class="services">
    <h2>Our Services</h2>
    <article class="service">
      <svg class="service-icon" viewBox="0 0 124 124"><circle cx="62" cy="62" r="60" fill="#fff" stroke="#0792cd" stroke-width="3"/><circle cx="62" cy="62" r="55" fill="#0792cd"/><path d="M36 64 H86 L80 73 H42 Z" fill="#fff"/><rect x="50" y="56" width="16" height="8" fill="#fff"/><path d="M66 58 L90 38" stroke="#fff" stroke-width="2"/><path d="M36 80 q6 -4 12 0 t12 0 t12 0 t12 0" fill="none" stroke="#fff" stroke-width="2.5"/><path d="M36 87 q6 -4 12 0 t12 0 t12 0 t12 0" fill="none" stroke="#fff" stroke-width="2.5"/></svg>
      <h3>Extensive knowledge of fishing</h3>
      <p>Sed ut perspiciatis unde omnis iste natus error sit voluptatem accusantium doloremque laudantium.</p>
      <a class="outline-btn" href="#">Read more</a>
    </article>
    <article class="service">
      <svg class="service-icon" viewBox="0 0 124 124"><circle cx="62" cy="62" r="60" fill="#fff" stroke="#0792cd" stroke-width="3"/><circle cx="62" cy="62" r="55" fill="#0792cd"/><path d="M32 82 L56 50 L64 60 L70 54 L92 82 Z" fill="#fff"/><path d="M60 54 V36" stroke="#fff" stroke-width="2"/><path d="M60 36 L72 39 L60 43 Z" fill="#fff"/></svg>
      <h3>Seasonality</h3>
      <p>Sed ut perspiciatis unde omnis iste natus error sit voluptatem accusantium doloremque laudantium.</p>
      <a class="outline-btn" href="#">Read more</a>
    </article>
    <article class="service">
      <svg class="service-icon" viewBox="0 0 124 124"><circle cx="62" cy="62" r="60" fill="#fff" stroke="#0792cd" stroke-width="3"/><circle cx="62" cy="62" r="55" fill="#0792cd"/><path d="M38 88 V58 L50 66 V58 L62 66 V58 L74 66 V48 H84 V88 Z" fill="#fff"/><rect x="44" y="74" width="6" height="6" fill="#0792cd"/><rect x="56" y="74" width="6" height="6" fill="#0792cd"/><rect x="68" y="74" width="6" height="6" fill="#0792cd"/><circle cx="78" cy="38" r="7" fill="#fff"/><circle cx="88" cy="34" r="6" fill="#fff"/></svg>
      <h3>Production and accreditations</h3>
      <p>Sed ut perspiciatis unde omnis iste natus error sit voluptatem accusantium doloremque laudantium.</p>
      <a class="outline-btn" href="#">Read more</a>
    </article>
  </section>

  <section class="contact">
    <div class="contact-bg" role="img" aria-label="Photo of a school of fish, tinted blue"></div>
    <h2>Contact Us</h2>
    <div class="contact-photo" role="img" aria-label="Photo of a person seated by the sea at sunset"></div>
    <ul class="contact-list">
      <li><svg viewBox="0 0 18 18"><rect x="1.5" y="3.5" width="15" height="11" fill="none" stroke="#fff" stroke-width="1.6"/><path d="M1.5 4 L9 10 L16.5 4" fill="none" stroke="#fff" stroke-width="1.6"/></svg>dagur@marvantar.is</li>
      <li><svg viewBox="0 0 18 18"><path d="M4 1.5 L7 5 L5.5 7 Q7 10.5 11 12.5 L13 11 L16.5 14 L14.5 16.5 Q7 16 1.5 4 Z" fill="#fff"/></svg>Tel: +3654170392</li>
    </ul>
  </section>

  <footer class="site-footer">© 2017 Marvantar.&nbsp; All right reserved . Term of Use</footer>
</body>
</html>
```